Software static HTML page design

We need 5 static HTML pages designed for our current software startup - TallyNest. All details are attached in a document for consideration.

Target Market(s)

Sporting clubs/University clubs

Industry/Entity Type

Software

Number of Pages Required

5+ page

Font styles to use
Sans Serif

Colors
33a6d7
85cae6
86cfc6
33b8a4
ffffff

```html
<!DOCTYPE html>
<html lang="en">
<head>
<meta charset="utf-8">
<title>TallyNest — Bringing your club to the social web</title>
<link rel="stylesheet" href="https://fonts.googleapis.com/css2?family=Raleway:wght@500;600;700&family=Open+Sans:wght@400;600;700&display=swap">
<style>
  :root {
    --blue: #33a6d7;
    --sky: #85cae6;
    --mint: #86cfc6;
    --teal: #33b8a4;
    --white: #ffffff;
    --lime: #a9c62a;
    --deep: #0a95c9;
    --ink: #222222;
    --grey-text: #666666;
    --field-line: #cccccc;
    --tab-off: #efefef;
    --social: #5a6fb3;
  }
  * { margin: 0; padding: 0; box-sizing: border-box; }
  html, body { width: 1200px; height: 672px; overflow: hidden; background: var(--white); }
  body { position: relative; font-family: "Open Sans", sans-serif; color: var(--ink); }

  .hero-backdrop { position: absolute; inset: 0; width: 1200px; height: 672px; }

  .brand {
    position: absolute; left: 99px; top: 34px; display: flex; align-items: center; gap: 8px;
    font-family: "Open Sans", sans-serif; font-weight: 700; font-size: 27px; color: var(--white); letter-spacing: .5px;
  }
  .brand-mark { width: 22px; height: 22px; background: var(--white); }

  .main-nav { position: absolute; top: 40px; left: 426px; display: flex; gap: 0; }
  .main-nav a {
    position: absolute; font-family: "Raleway", sans-serif; font-weight: 500; font-size: 15px;
    color: var(--white); text-decoration: none; white-space: nowrap;
  }
  .main-nav .is-active::after {
    content: ""; position: absolute; left: 0; right: 0; bottom: -6px; height: 2px; background: var(--white);
  }
  .nav-search { position: absolute; left: 829px; top: 42px; }

  .account-btn {
    position: absolute; top: 36px; height: 34px; border: 1px solid var(--white); border-radius: 18px;
    display: flex; align-items: center; justify-content: center; gap: 6px;
    color: var(--white); font-weight: 700; font-size: 14px; letter-spacing: .3px;
  }
  .account-btn.login { left: 888px; width: 101px; }
  .account-btn.signup { left: 999px; width: 101px; }

  .headline {
    position: absolute; left: 97px; top: 240px; width: 520px;
    font-family: "Raleway", sans-serif; font-weight: 700; font-size: 37px; line-height: 52px;
    color: var(--white); text-shadow: 0 2px 4px rgba(0,0,0,.18);
  }
  .cta-outline {
    position: absolute; left: 99px; top: 371px; width: 173px; height: 47px;
    border: 1px solid var(--white); border-radius: 24px; display: flex; align-items: center; justify-content: center;
    color: var(--white); font-weight: 700; font-size: 14px; letter-spacing: .3px;
  }

  .auth-card {
    position: absolute; left: 681px; top: 141px; width: 419px; height: 421px;
    background: var(--white); padding: 3px; box-shadow: 0 1px 6px rgba(0,0,0,.18);
  }
  .auth-tabs { display: flex; height: 52px; }
  .auth-tab {
    flex: 1; display: flex; align-items: center; justify-content: center;
    font-weight: 600; font-size: 21px; color: var(--ink); background: var(--tab-off);
  }
  .auth-tab.is-active { background: var(--blue); color: var(--white); }

  .social-login {
    position: absolute; left: 89px; top: 89px; width: 241px; height: 45px; border-radius: 3px;
    background: var(--social); color: var(--white); display: flex; align-items: center; gap: 10px;
    padding-left: 12px; font-weight: 600; font-size: 16px;
  }
  .social-login-square { width: 28px; height: 28px; background: var(--white); }
  .divider-or { position: absolute; left: 0; right: 0; top: 158px; text-align: center; font-size: 14px; color: var(--grey-text); }

  .field {
    position: absolute; left: 22px; width: 376px; height: 47px; border: 1px solid var(--field-line);
    padding-left: 16px; display: flex; align-items: center; font-size: 14px; color: var(--grey-text);
  }
  .field.email { top: 199px; }
  .field.password { top: 268px; }

  .submit-btn {
    position: absolute; left: 21px; top: 340px; width: 126px; height: 47px; border-radius: 24px;
    background: var(--teal); color: var(--white); display: flex; align-items: center; justify-content: center;
    font-weight: 700; font-size: 17px; letter-spacing: .5px; box-shadow: 0 1px 3px rgba(0,0,0,.2);
  }
  .forgot-link { position: absolute; right: 21px; top: 355px; font-weight: 600; font-size: 12px; color: #555555; }

  .copyright { position: absolute; right: 100px; top: 613px; font-size: 13px; color: var(--grey-text); }
</style>
</head>
<body>
  <svg class="hero-backdrop" viewBox="0 0 1200 672" role="img" aria-label="Sports venue photo with a faint network of connected points, tinted green to blue">
    <defs>
      <linearGradient id="heroTint" x1="0" y1="0" x2="1" y2="1">
        <stop offset="0" stop-color="#a9c62a"/>
        <stop offset=".35" stop-color="#5bbb6a"/>
        <stop offset=".65" stop-color="#17b5c3"/>
        <stop offset="1" stop-color="#0a8fd0"/>
      </linearGradient>
    </defs>
    <rect width="1200" height="672" fill="url(#heroTint)"/>
    <polygon points="0,672 1200,428 1200,672" fill="#ffffff"/>
  </svg>

  <div class="brand"><span class="brand-mark"></span>TallyNest</div>

  <nav class="main-nav">
    <a class="is-active" style="left:0;top:0">HOME</a>
    <a style="left:82px;top:0">FEATURES</a>
    <a style="left:196px;top:0">PRICING</a>
    <a style="left:294px;top:0">CONTACT</a>
  </nav>
  <svg class="nav-search" width="14" height="14" viewBox="0 0 14 14" aria-label="Search">
    <circle cx="5.8" cy="5.8" r="4.3" fill="none" stroke="#fff" stroke-width="2"/>
    <line x1="9" y1="9" x2="13" y2="13" stroke="#fff" stroke-width="2.2" stroke-linecap="round"/>
  </svg>

  <div class="account-btn login">
    <svg width="10" height="12" viewBox="0 0 10 12"><rect x="0" y="5" width="10" height="7" rx="1" fill="#fff"/><path d="M2.5 5V3.5a2.5 2.5 0 0 1 5 0V5" fill="none" stroke="#fff" stroke-width="1.6"/></svg>
    LOGIN
  </div>
  <div class="account-btn signup">
    <svg width="13" height="13" viewBox="0 0 13 13"><path d="M1 12l1-3.5 7-7 2.5 2.5-7 7z" fill="#fff"/></svg>
    SIGN UP
  </div>

  <h1 class="headline">BRINGING YOUR CLUB TO THE SOCIAL WEB</h1>
  <div class="cta-outline">FIND OUT MORE</div>

  <section class="auth-card">
    <div class="auth-tabs">
      <div class="auth-tab is-active">LOGIN</div>
      <div class="auth-tab">SIGN UP</div>
    </div>
    <div class="social-login"><span class="social-login-square"></span>Login with Linkfolk</div>
    <div class="divider-or">OR</div>
    <div class="field email">yours@example.com</div>
    <div class="field password">Password</div>
    <div class="submit-btn">LOGIN</div>
    <div class="forgot-link">Don't remember your password?</div>
  </section>

  <p class="copyright">Copyright © 2017, TallyNest. All right reserved.</p>
</body>
</html>
```